The Little Sprout Gathering -Flyer Design

The flyer is for a conference that is being held for Chiropractors to gain continuing education in paediatrics with all proceeds from the event going to paediatric research.

Paediatric chiropractic is mostly about how we can help the body and brain develop optimally with a big focus of the nervous system. I have attached the logo and the website is www.littlesproutgathering.example. The feel should be kid friendly but also professional. It is also going to be largely for the American Market.

Here is an outline of the copy that we need on this flyer:
========================================
Don’t Miss This….some of the best minds in Chiropractic Pediatrics…all together in the USA.

23-24th April 2016, San Francisco. Sat 23rd 8.30-5.30 Sun 24th 8.30am -1pm

Harborline Lodge by Brennard, ​Bayview Terminal-Pierside

With all proceeds going directly to Pediatric based research projects at the Institute for Spinal Wellness Studies at QVSI.

Learn From:

Dr. Marlene Vostrik
Dr. Ilse Fenwarr
Dr. Petra Lindqvol
Dr. Rosalind Pettow
Dr. Tommy Merravin
Dr. Annabelle Throssel
Dr. Josephine Throssel
Dr. Greta Molloru
Dr. Nora Falby
Dr. Miriam Pask

Early bird $449 18th Mar 2016

CE available

More info at www.littlesproutgathering.example (could we also have a Facebook icon too!)

```html
<!DOCTYPE html>
<html lang="en">
<head>
<meta charset="utf-8">
<title>The Little Sprout Gathering – Flyer</title>
<link href="https://fonts.googleapis.com/css2?family=Anton&family=Oswald:wght@600&family=Quicksand:wght@400;600&family=Lato:wght@400;700&family=Tinos&display=swap" rel="stylesheet">
<style>
  :root{
    --backdrop:#161616;
    --orange-deep:#e0531f;
    --orange:#ee6428;
    --orange-soft:#f58a4f;
    --paper:#ffffff;
    --paper-shade:#d9d9d9;
    --ink:#2b2b2b;
    --olive:#6d705c;
    --green:#78a22a;
    --square:#3b5a98;
  }
  *{box-sizing:border-box;margin:0;padding:0}
  html,body{width:1200px;height:840px;overflow:hidden;background:var(--backdrop)}
  .flyer{
    position:absolute;left:330px;top:40px;width:540px;height:760px;
    background:linear-gradient(180deg,var(--paper) 55%,var(--paper-shade) 100%);
    overflow:hidden;
  }
  .flyer-shapes{position:absolute;inset:0}
  .curved-text{font-family:"Lato",sans-serif;font-weight:700;font-size:15px;fill:var(--paper);letter-spacing:.2px}
  .headline{
    position:absolute;left:0;right:0;top:58px;text-align:center;
    font-family:"Anton",sans-serif;color:var(--paper);font-size:66px;line-height:70px;
    padding-left:50px;
  }
  .tagline{
    position:absolute;left:0;right:0;top:212px;text-align:center;padding-left:70px;
    font-family:"Quicksand",sans-serif;color:var(--paper);font-size:19px;line-height:24px;
  }
  .event-info{position:absolute;left:0;right:0;top:420px;text-align:center;color:var(--ink)}
  .brand{
    display:flex;align-items:center;justify-content:center;gap:12px;
    font-family:"Quicksand",sans-serif;font-weight:600;font-size:30px;color:var(--orange);
    margin-bottom:14px;
  }
  .brand-dot{width:22px;height:22px;border-radius:50%;background:var(--orange)}
  .dates{font-family:"Tinos",serif;font-size:22px;line-height:26px}
  .times{font-family:"Tinos",serif;font-size:19px;line-height:24px}
  .venue{font-family:"Tinos",serif;font-size:13px;margin-top:4px}
  .speakers{margin-top:16px;font-family:"Lato",sans-serif;color:var(--orange)}
  .speakers h2{font-weight:400;font-size:15px;margin-bottom:4px}
  .speakers p{font-size:10.5px;line-height:15px}
  .pricing{margin-top:18px;font-family:"Oswald",sans-serif;font-weight:600}
  .early-bird{font-size:22px;color:var(--olive)}
  .ce{font-size:19px;color:var(--green)}
  .more-info{
    margin-top:10px;display:flex;align-items:center;justify-content:center;gap:8px;
    font-family:"Lato",sans-serif;font-weight:700;font-size:12px;color:var(--ink);
  }
  .social-square{width:15px;height:15px;background:var(--square)}
</style>
</head>
<body>
<main class="flyer">
  <svg class="flyer-shapes" width="540" height="760" viewBox="0 0 540 760">
    <defs>
      <linearGradient id="header-fill" x1="0" y1="0" x2="1" y2="1">
        <stop offset="0" stop-color="#e0531f"/>
        <stop offset="0.55" stop-color="#ee6428"/>
        <stop offset="1" stop-color="#f07a3c"/>
      </linearGradient>
      <path id="proceeds-line-1" d="M20 318 C160 300 360 310 530 355"/>
      <path id="proceeds-line-2" d="M30 340 C170 322 360 332 530 377"/>
    </defs>
    <path d="M0 0 H540 V410 C420 360 300 345 180 352 C110 356 50 366 0 378 Z" fill="url(#header-fill)" role="img" aria-label="Orange header with soft flame-like swirl decoration"/>
    <path d="M0 378 C50 366 110 356 180 352 C300 345 420 360 540 410 V424 C420 376 300 362 180 368 C110 372 50 382 0 394 Z" fill="#ececec"/>
    <path class="dashed-ring" d="M215 50 A150 150 0 0 0 149 231" fill="none" stroke="#fff" stroke-width="2" stroke-dasharray="7 6"/>
    <path class="dashed-ring" d="M380 60 A150 150 0 0 1 431 231" fill="none" stroke="#fff" stroke-width="2" stroke-dasharray="7 6"/>
    <text class="curved-text"><textPath href="#proceeds-line-1">With all proceeds going directly to Pediatric based research</textPath></text>
    <text class="curved-text"><textPath href="#proceeds-line-2">projects at the Institute for Spinal Wellness Studies at QVSI</textPath></text>
  </svg>

  <h1 class="headline">Don’t<br>Miss This..</h1>
  <p class="tagline">some of the best minds<br>in Chiropractic Pediatrics...<br>all together in the USA.</p>

  <section class="event-info">
    <div class="brand"><span class="brand-dot"></span>The Little Sprout Gathering</div>
    <p class="dates">23-24<sup>th</sup> April 2016, San Francisco.</p>
    <p class="times">Sat 23<sup>rd</sup> 8.30-5.30 Sun 24<sup>th</sup> 8.30am -1pm</p>
    <p class="venue">Harborline Lodge by Brennard, Bayview Terminal-Pierside</p>
    <div class="speakers">
      <h2>Learn From..</h2>
      <p>Dr. Marlene Vostrik | Dr. Ilse Fenwarr | Dr. Petra Lindqvol | Dr. Rosalind Pettow | Dr. Tommy Merravin</p>
      <p>Dr. Annabelle Throssel | Dr. Josephine Throssel | Dr. Greta Molloru | Dr. Nora Falby | Dr. Miriam Pask</p>
    </div>
    <div class="pricing">
      <p class="early-bird">Early bird $449 18<sup>th</sup> Mar 2016</p>
      <p class="ce">CE available</p>
    </div>
    <p class="more-info">More info at www.littlesproutgathering.example <span class="social-square"></span></p>
  </section>
</main>
</body>
</html>
```